Product flyer with pricing

We manufacture iconic and luxury vending trailers. for our first trailer we need a flyer created to give to prospective clients with base pricing. I am uploading an example along with graphic files.

```html
<!DOCTYPE html>
<html lang="en">
<head>
<meta charset="utf-8">
<title>Meadow Cottage Mini – Flyer</title>
<link href="https://fonts.googleapis.com/css2?family=Arimo:wght@400;700&display=swap" rel="stylesheet">
<style>
  :root{
    --orange:#ef9f27;
    --orange-panel:#f0aa2d;
    --green:#67a446;
    --green-line:#5e9d3f;
    --text:#3f3f3f;
    --white:#ffffff;
    --sky-top:#5f8fd0;
    --sky-bottom:#c9d3dc;
  }
  *{margin:0;padding:0;box-sizing:border-box}
  html,body{width:927px;height:1200px;overflow:hidden;background:var(--white)}
  body{font-family:"Arimo",Arial,sans-serif;color:var(--text)}
  .flyer{position:relative;width:927px;height:1200px;overflow:hidden;background:var(--white)}

  .brand{position:absolute;left:96px;top:76px;width:200px;display:flex;align-items:center;gap:8px;white-space:nowrap}
  .brand-dot{flex:none;width:18px;height:18px;border-radius:50%;background:var(--green)}
  .brand-name{font-weight:700;font-size:17px;color:var(--orange);letter-spacing:.3px}

  .headline{position:absolute;left:316px;top:52px}
  .headline h1{font-size:39px;font-weight:700;color:var(--orange);line-height:1.1;letter-spacing:-.3px}
  .headline h1 .lead{color:var(--green);font-size:29px}
  .headline .tagline{font-size:27px;font-weight:700;color:var(--green);margin-top:2px}

  .gallery{position:absolute;top:149px;left:0;width:927px;height:184px}
  .gallery .photo{position:absolute;top:0;height:184px;background:linear-gradient(180deg,var(--sky-top) 0%,#8eb0dc 40%,#eef0f2 55%,#6b6f74 80%,var(--sky-bottom) 100%)}
  .photo-1{left:0;width:228px}
  .photo-2{left:234px;width:226px}
  .photo-3{left:467px;width:227px}
  .photo-4{left:700px;width:227px}

  .price-badge{position:absolute;left:624px;top:322px;width:128px;height:128px}
  .price-badge .label{position:absolute;inset:0;display:flex;flex-direction:column;align-items:center;justify-content:center;color:var(--white);font-weight:700}
  .price-badge .small{font-size:15px}
  .price-badge .amount{font-size:26px;margin-top:1px}

  .features{position:absolute;left:91px;top:386px}
  .section-title{font-size:27px;font-weight:700}
  .features .section-title{color:var(--orange)}
  .bullets{list-style:none}
  .features .bullets{margin-top:23px;width:730px}
  .bullets li{position:relative;padding-left:18px;font-size:17.5px;line-height:21px}
  .bullets li::before{content:"";position:absolute;left:1px;top:7px;width:6px;height:6px;border-radius:50%;background:var(--green)}
  .features .bullets li{margin-bottom:19px}

  .rule-green{position:absolute;left:530px;top:712px;width:397px;height:6px;background:var(--green-line)}
  .rule-orange{position:absolute;left:0;top:756px;width:530px;height:6px;background:var(--orange-panel)}

  .options-panel{position:absolute;left:0;top:772px;width:530px;height:428px;background:var(--green);color:var(--white)}
  .options-panel .section-title{position:absolute;left:91px;top:50px;font-size:28px}
  .options-panel .bullets{position:absolute;left:91px;top:110px;width:360px}
  .options-panel .bullets li{margin-bottom:15px;font-size:17.5px}
  .options-panel .bullets li::before{background:var(--orange-panel)}

  .uses-panel{position:absolute;left:530px;top:726px;width:397px;height:474px;background:var(--orange-panel);color:var(--white)}
  .uses-panel .section-title{position:absolute;left:48px;top:60px;font-size:28px}
  .uses-panel .bullets{position:absolute;left:48px;top:123px;width:290px}
  .uses-panel .bullets li{margin-bottom:17px;font-size:17.5px}
  .uses-panel .bullets li::before{background:var(--white)}
  b{font-weight:700}
</style>
</head>
<body>
<main class="flyer">
  <div class="brand">
    <span class="brand-dot"></span>
    <span class="brand-name">SUNBEAM CABINS</span>
  </div>

  <header class="headline">
    <h1><span class="lead">The </span>“Meadow Cottage Mini”</h1>
    <p class="tagline">Luxury, mobile vending house</p>
  </header>

  <section class="gallery">
    <div class="photo photo-1" role="img" aria-label="White board-and-batten vending house on a trailer, side view with pickup truck"></div>
    <div class="photo photo-2" role="img" aria-label="Front gable view of the vending house with black door and window"></div>
    <div class="photo photo-3" role="img" aria-label="Side view of the vending house on tandem-axle trailer"></div>
    <div class="photo photo-4" role="img" aria-label="Vending house with serving window opened"></div>
  </section>

  <div class="price-badge">
    <svg width="128" height="128" viewBox="0 0 128 128" aria-hidden="true">
      <g fill="var(--orange)" transform="translate(64 64)">
        <rect x="-44" y="-44" width="88" height="88"/>
        <rect x="-44" y="-44" width="88" height="88" transform="rotate(15)"/>
        <rect x="-44" y="-44" width="88" height="88" transform="rotate(30)"/>
        <rect x="-44" y="-44" width="88" height="88" transform="rotate(45)"/>
        <rect x="-44" y="-44" width="88" height="88" transform="rotate(60)"/>
        <rect x="-44" y="-44" width="88" height="88" transform="rotate(75)"/>
      </g>
      <circle cx="64" cy="64" r="52" fill="var(--green)"/>
    </svg>
    <div class="label"><span class="small">Base price:</span><span class="amount">$45,000</span></div>
  </div>

  <section class="features">
    <h2 class="section-title">Base unit features:</h2>
    <ul class="bullets">
      <li>Trailer features tandem wheels w/ brakes</li>
      <li>Steel frame construction for fire retardation safety and weight reduction.</li>
      <li>100% off grid with solar and lithium battery system allowing the trailer to be used<br>in places not accessible by traditional trailers.</li>
      <li>80 gallon water supply tank</li>
      <li>100 gallon waste water tank</li>
      <li>Cupboards, cabinets &amp; four stainless steel sinks.</li>
      <li>60” Gas shock serving window</li>
    </ul>
  </section>

  <div class="rule-green"></div>
  <div class="rule-orange"></div>

  <section class="options-panel">
    <h2 class="section-title">Available options:</h2>
    <ul class="bullets">
      <li>HVAC - Nordair Mini Split - <b>$1,800</b></li>
      <li>Cooler / Glass front Commercial<br>refrigerator - <b>$1,600</b></li>
      <li>Upper loft storage area - <b>$1,200</b></li>
      <li>Signage and graphics - <b>$2,000 - $5,000</b><br>depend on complexity</li>
      <li>Ice machine - <b>$1,100</b></li>
      <li>Other custom items available on request.</li>
    </ul>
  </section>

  <section class="uses-panel">
    <h2 class="section-title">Use cases:</h2>
    <ul class="bullets">
      <li>Food: Lemonade, Coffee,<br>pizza, cookies, doughnuts,<br>barbecue and more!</li>
      <li>Retail: Clothing, watches,<br>jewelry, flowers and more!</li>
      <li>Corporate: Product info,<br>demonstration, information,<br>brand awareness.</li>
      <li>Fundraisers: Girls/boy sports,<br>non profits, etc.</li>
    </ul>
  </section>
</main>
</body>
</html>
```